QX27

We want a trendy packaging design for our mobile accessories. Initially we will be offering TPU cases to our retail customers and than we will introduce other similar accessories such as car chargers, AC chargers, data cables etc..
We would like to see designs that are unique, practical and appealing to the general audience.
Updates

Hi Everyone

There is guaranteed payment for the best designer of this packaging.

thanks

Reason: Hi All This will give you all more time to submit your designs :) regards

Target Market(s)

Telco retail store customers

Industry/Entity Type

Retail

Requirements
Must have
• Colorful , Fun , Sexy

```html
<!DOCTYPE html>
<html lang="en">
<head>
<meta charset="utf-8">
<title>QX27 Case Packaging</title>
<link href="https://fonts.googleapis.com/css2?family=Ubuntu:wght@400;500&display=swap" rel="stylesheet">
<style>
  :root {
    --page-bg: #c9c6c6;
    --box-white: #f4f3f3;
    --brand-green: #3d6b2b;
    --leaf-green: #7bb239;
    --leaf-yellow: #f2e14a;
    --leaf-orange: #f0a23a;
    --leaf-blue: #5ab8d8;
    --case-pink: #c25fc3;
    --screen-grey: #d9dbe0;
  }
  * { margin: 0; padding: 0; box-sizing: border-box; }
  html, body {
    width: 1200px;
    height: 1084px;
    overflow: hidden;
    background: var(--page-bg);
  }
  .package {
    position: absolute;
    left: 250px;
    top: 42px;
    width: 700px;
    height: 1000px;
    background: var(--box-white);
    overflow: hidden;
    box-shadow: 0 6px 24px rgba(0,0,0,0.25);
  }
  .pattern-top {
    position: absolute;
    left: 0; top: 0;
    width: 700px;
    height: 224px;
    background: linear-gradient(135deg, var(--leaf-green) 0%, var(--leaf-yellow) 35%, var(--leaf-green) 60%, var(--leaf-blue) 80%, var(--leaf-green) 100%);
  }
  .pattern-top::after {
    content: "";
    position: absolute;
    left: 0; bottom: 0;
    width: 100%;
    height: 18px;
    background: var(--leaf-orange);
  }
  .pattern-bottom {
    position: absolute;
    left: 0; top: 780px;
    width: 700px;
    height: 220px;
  }
  .product-window {
    position: absolute;
    left: 91px;
    top: 79px;
    width: 540px;
    height: 662px;
    border-radius: 42px;
    border: 10px solid #ffffff;
    background: linear-gradient(100deg, var(--case-pink) 0%, #d07bd2 55%, var(--screen-grey) 62%, #bcd0e4 78%, #9fbf5a 100%);
    box-shadow: inset 0 0 18px rgba(0,0,0,0.2), 0 2px 8px rgba(0,0,0,0.15);
  }
  .brand {
    position: absolute;
    left: 372px;
    top: 758px;
    font-family: "Ubuntu", sans-serif;
    color: var(--brand-green);
  }
  .brand-name {
    font-size: 46px;
    font-weight: 400;
    line-height: 1;
  }
  .brand-sub {
    display: block;
    margin-top: 2px;
    margin-left: 44px;
    font-size: 10px;
    font-weight: 500;
    letter-spacing: 4px;
  }
  .model-code {
    position: absolute;
    left: 540px;
    top: 774px;
    font-family: "Ubuntu", sans-serif;
    font-size: 26px;
    font-weight: 500;
    color: var(--brand-green);
  }
</style>
</head>
<body>
  <div class="package">
    <div class="pattern-top" role="img" aria-label="Colourful swirling floral pattern in green, yellow, blue and orange"></div>

    <svg class="pattern-bottom" viewBox="0 0 700 220" role="img" aria-label="Colourful floral pattern rising from the bottom edge in green, yellow, orange and blue">
      <defs>
        <linearGradient id="floral-tones" x1="0" y1="0" x2="1" y2="1">
          <stop offset="0" stop-color="#f2e14a"/>
          <stop offset="0.35" stop-color="#7bb239"/>
          <stop offset="0.65" stop-color="#f0a23a"/>
          <stop offset="1" stop-color="#7bb239"/>
        </linearGradient>
      </defs>
      <path d="M0 80 C60 50 110 60 160 90 C200 40 250 20 300 60 C340 30 380 40 420 80 C470 30 520 40 560 70 C610 40 660 50 700 60 L700 220 L0 220 Z" fill="url(#floral-tones)"/>
    </svg>

    <div class="product-window" role="img" aria-label="Product photo of a pink polka-dot phone case beside a smartphone"></div>

    <div class="brand">
      <div class="brand-name">Zesty</div>
      <span class="brand-sub">GADGETS</span>
    </div>
    <div class="model-code">QX27</div>
  </div>
</body>
</html>
```